Hot young IT advisor needs business cards as upscale and innovative as they are

We need business cards that make a statement about who we are, as a young and upscale IT advisor. Our whole angle is innovation and tenacity in our personal relationships with our clients. We've just done a brand overhaul and need cards that have the new logos, but we're also looking for someone with a sixth sense who can capture what sets us apart and communicate that with a business card. Clean, minimalist, upscale, innovative, personal. Our budget only allows room for them to be soft-touch, no spot gloss or foil designs please.

Target Market(s)

High-level decision makers at middle-market and large organizations in the healthcare, financial services, sports and entertainment, K-12 education, college and university, state and local government, and federal government sectors.

Industry/Entity Type

Information Technology

Font styles to use
Sans Serif

Colors
ec1f27
606060
ffffff

Requirements
Should not have
• Designs with low contrast which would require spot-gloss or embossing.

```html
<!DOCTYPE html>
<html lang="en">
<head>
<meta charset="utf-8">
<title>Vantora — Business Card</title>
<link rel="stylesheet" href="https://fonts.googleapis.com/css2?family=Montserrat:wght@500&family=Roboto:wght@400;500&display=swap">
<style>
  :root {
    --brand-red: #ec1f27;
    --brand-grey: #606060;
    --ink: #333333;
    --paper: #ffffff;
    --paper-shade: #f1f1f1;
    --stage: #000000;
  }
  * { margin: 0; padding: 0; box-sizing: border-box; }
  html, body { width: 900px; height: 1200px; overflow: hidden; background: var(--stage); }
  .canvas { position: relative; width: 900px; height: 1200px; }
  .card {
    position: absolute; left: 80px; width: 733px; height: 429px;
    border-radius: 28px; overflow: hidden;
  }
  .card--front { top: 128px; background: radial-gradient(ellipse at 75% 40%, var(--paper) 30%, var(--paper-shade) 100%); }
  .card--back { top: 646px; background: var(--paper); }

  .brand-decoration {
    position: absolute; left: 54px; top: 0; width: 302px; height: 418px;
    background: linear-gradient(180deg, rgba(236,31,39,0.35) 0%, var(--brand-red) 50%, rgba(96,96,96,0.75) 100%);
    clip-path: polygon(0 0, 100% 0, 100% 100%, 226px 100%, 226px 270px, 0 270px);
  }

  .wordmark {
    font-family: "Montserrat", sans-serif; font-weight: 500;
    color: var(--ink); letter-spacing: 0.14em; line-height: 1;
  }
  .card--front .wordmark { position: absolute; left: 408px; top: 111px; font-size: 33px; }

  .address, .contact-list, .person {
    position: absolute; font-family: "Roboto", sans-serif; color: var(--ink); font-style: normal;
  }
  .address { left: 409px; top: 163px; font-size: 16.5px; line-height: 22.5px; }
  .contact-list { left: 409px; top: 245px; list-style: none; font-size: 16.5px; line-height: 23px; }
  .contact-list li { display: flex; align-items: center; gap: 9px; }
  .contact-icon { width: 19px; height: 19px; flex: none; }

  .person { left: 54px; top: 329px; }
  .person-name { font-size: 20px; font-weight: 500; line-height: 26px; }
  .person-role { font-size: 16.5px; color: var(--brand-red); line-height: 22px; }

  .back-lockup {
    position: absolute; left: 0; right: 0; top: 280px;
    display: flex; justify-content: center; align-items: center; gap: 14px;
  }
  .back-lockup .mark-square { width: 20px; height: 20px; background: var(--brand-red); }
  .card--back .wordmark { font-size: 34px; }
</style>
</head>
<body>
<main class="canvas">
  <section class="card card--front">
    <div class="brand-decoration" role="img" aria-label="Brand decoration area in red and grey tones"></div>

    <div class="wordmark">VANTORA</div>

    <address class="address">118 Larkspur Avenue NE<br>Suite 300, Fairhaven<br>MI 49010</address>

    <ul class="contact-list">
      <li>
        <svg class="contact-icon" viewBox="0 0 20 20" aria-hidden="true"><circle cx="10" cy="10" r="10" fill="#ec1f27"/><path d="M7 5.5l2 2-1.2 1.3c.7 1.4 1.8 2.5 3.3 3.3l1.3-1.2 2 2-1.3 1.6c-3.4-.4-6.8-3.8-7.2-7.3z" fill="#fff"/></svg>
        555-014-2620
      </li>
      <li>
        <svg class="contact-icon" viewBox="0 0 20 20" aria-hidden="true"><circle cx="10" cy="10" r="10" fill="#ec1f27"/><rect x="5" y="6.5" width="10" height="7" fill="none" stroke="#fff" stroke-width="1.4"/><path d="M5 6.8l5 3.7 5-3.7" fill="none" stroke="#fff" stroke-width="1.4"/></svg>
        info@vantora.com
      </li>
      <li>
        <svg class="contact-icon" viewBox="0 0 20 20" aria-hidden="true"><circle cx="10" cy="10" r="10" fill="#ec1f27"/><g fill="none" stroke="#fff" stroke-width="1.2"><circle cx="10" cy="10" r="5.5"/><ellipse cx="10" cy="10" rx="2.4" ry="5.5"/><path d="M4.5 10h11M5.3 7.3h9.4M5.3 12.7h9.4"/></g></svg>
        www.yourwebsitehere.com
      </li>
    </ul>

    <div class="person">
      <div class="person-name">Julian Mercer</div>
      <div class="person-role">Managing Director</div>
    </div>
  </section>

  <section class="card card--back">
    <div class="back-lockup">
      <span class="mark-square" aria-hidden="true"></span>
      <span class="wordmark">VANTORA</span>
    </div>
  </section>
</main>
</body>
</html>
```